Brochure Design Project

Hi I just need a brochure put together over 4 - 5 pages.
I will send you the logo, pictures, about us, services, and any other information. I just need it put together in a clean crisp professional way.
Front page should have logo and the first photo i upload of this building with contact details
T :1300 562 071
M: 0438217096
F :1900 347 615
E: enquiries@harbourquarrycraft.com.au
Second page should have services which you can find on my website www.harbourquarrycraft.com.au
Second page should have a list of previous work which you can find on the website www.harbourquarrycraft.com.au
Third page should have about us with our photos which you can find on the website. www.harbourquarrycraft.com.au
Fourth page should have a page with photos of previous work which you can find on the website and i will upload some photos on here.
Reason: Want to get some feedback from friends and make a few changes.
Target Market(s)
Builders in sydney.
Some residential customers aswell
Industry/Entity Type
Building
Requirements
Must have
- Double banded golden border running around the edge of each page.
1300 562 071 number visible on every page on top right or left corner.

```html
<!DOCTYPE html>
<html lang="en">
<head>
<meta charset="utf-8">
<title>Harbour Quarrycraft – Brochure Spread</title>
<link rel="stylesheet" href="https://fonts.googleapis.com/css2?family=Fira+Sans:ital,wght@0,300;0,400;1,300;1,400&display=swap">
<style>
  :root {
    --brown: #4b2a1b;
    --gold: #f6b91c;
    --gold-soft: #f8c64a;
    --text: #3d3d3d;
    --rule: #d9d6cf;
    --paper: #ffffff;
  }
  * { margin: 0; padding: 0; box-sizing: border-box; }
  html, body { width: 1200px; height: 927px; overflow: hidden; background: var(--paper); }
  body { font-family: "Fira Sans", Arial, sans-serif; color: var(--text); position: relative; }

  .top-band {
    position: absolute; left: 0; top: 0; width: 1200px; height: 36px;
    background: var(--brown);
    display: flex; justify-content: space-between; align-items: center;
    padding: 0 28px; font-size: 13.5px; font-weight: 400; color: var(--gold-soft);
  }
  .top-band .phone { font-style: italic; font-weight: 400; color: var(--gold); }

  .column-rule { position: absolute; top: 36px; width: 1px; height: 855px; background: var(--rule); }
  .column-rule.first { left: 401px; }
  .column-rule.second { left: 800px; }

  .panel { position: absolute; top: 96px; }
  .panel.work { left: 28px; width: 364px; }
  .panel.services { left: 428px; width: 340px; }
  .panel.about { left: 832px; width: 341px; }

  .panel-title {
    font-weight: 300; font-size: 44px; color: var(--gold);
    line-height: 58px; letter-spacing: 0.3px; margin-bottom: 33px;
  }

  .bullet-list { list-style: none; font-size: 13.5px; font-weight: 300; }
  .bullet-list li {
    position: relative; padding-left: 13px; line-height: 23px; margin-bottom: 4px;
  }
  .services .bullet-list li { padding-left: 20px; }
  .bullet-list li::before {
    content: ""; position: absolute; left: 1px; top: 10px;
    width: 3px; height: 3px; border-radius: 50%; background: #777;
  }
  .services .bullet-list li::before { left: 3px; }
  .bullet-list .site { font-style: italic; }

  .about-copy p {
    font-size: 13.5px; font-weight: 300; line-height: 22.8px;
    text-align: justify; hyphens: auto; -webkit-hyphens: auto; margin-bottom: 22px;
  }

  .team { position: absolute; top: 684px; left: 873px; display: flex; gap: 18px; }
  .member { width: 118px; text-align: center; font-size: 12.5px; font-weight: 300; line-height: 18px; }
  .member .portrait { display: block; width: 98px; height: 100px; margin: 0 auto 14px; }
  .member .role { font-style: italic; }

  .web { position: absolute; top: 869px; font-size: 13.5px; font-weight: 300; }
  .web.left { left: 28px; }
  .web.right { right: 28px; }

  .bottom-band { position: absolute; left: 0; width: 1200px; background: var(--gold); }
  .bottom-band.outer { top: 893px; height: 17px; }
  .bottom-band.inner { top: 913px; height: 14px; }
</style>
</head>
<body>
  <header class="top-band">
    <span class="brand">Harbour Quarrycraft <span class="phone">1300 562 071</span></span>
    <span class="brand">Harbour Quarrycraft <span class="phone">1300 562 071</span></span>
  </header>

  <div class="column-rule first"></div>
  <div class="column-rule second"></div>

  <section class="panel work">
    <h2 class="panel-title">Previous Work</h2>
    <ul class="bullet-list">
      <li><span class="site">Gallery of Modern Craft the Wharves</span>–Restoration/<br>Granite Marbel Fixing/Repointing (Kestrel Build)</li>
      <li><span class="site">Arden Court</span>–Restoration (State Works)</li>
      <li><span class="site">Millbrook Court House</span>–Construction (State Works)</li>
      <li><span class="site">Harrowgate Park</span>–Restoration (State Works)</li>
      <li><span class="site">Tallow Road</span>–The wharves–Restoration<br>(Coastal Services Board)</li>
      <li><span class="site">Linden House Hostel</span>–Restoration<br>(Housing Office)</li>
      <li><span class="site">Governor's Lodge</span>–Restoration (State Works)</li>
      <li><span class="site">East Harbour Technical College</span>–Restoration<br>(State Works)</li>
      <li><span class="site">Harbour Institute of Technology</span>–Epoxy Patching<br>(State Works )</li>
      <li><span class="site">Governor's Lodge</span>–Repointing and Fixing<br>(State Works)</li>
      <li><span class="site">Royal Harbour Gardens</span>–(State works )</li>
      <li><span class="site">Harbour University</span>–New Stonework &amp; Restoration<br>(Harbour University)</li>
      <li><span class="site">Brennan Park</span>–Westmere Council</li>
      <li><span class="site">Innovation Park</span>–Ashcombe St.</li>
      <li><span class="site">Fountain Restoration</span>–Harbour University</li>
      <li><span class="site">No. 9 Marlowe St.</span>–Atrium–Morland Voss &amp; Assoc.</li>
    </ul>
  </section>

  <section class="panel services">
    <h2 class="panel-title">Services</h2>
    <ul class="bullet-list">
      <li>Heritage Restoration</li>
      <li>Epoxy Patching / Stone Imitation</li>
      <li>Feature Walls</li>
      <li>Retaining Walls</li>
      <li>Steps</li>
      <li>Arches</li>
      <li>Marble and Granite Fixing</li>
      <li>Mechanical Fixing</li>
      <li>Paving</li>
      <li>Pointing</li>
    </ul>
  </section>

  <section class="panel about">
    <h2 class="panel-title">About Us</h2>
    <div class="about-copy" lang="en">
      <p>Callum Ferrier has been working both in London and Sydney over the last 15 years, following a family tradition started by his father Graham back in the 1960's. Callum served his apprenticeship in Sydney under the watchful eye of his father Graham. Once qualified, Callum subsequently worked as a freelance stonemason, where his skills were soon to be acknowledged and sought after by many of the established stone masons both in Sydney and London.</p>
      <p>Callum decided Sydney needed not only the services of a firm of first class stone masons, but a company who would understand Sydney's heritage, a company that was prepared to listen. This is when Harbour Quarrycraft was established.</p>
      <p>A combined 65 years of industry experience, Graham and Callum use the finest materials and embodygood old-fashioned values to ensure each assignment undertaken produce results of true distinction.</p>
    </div>
  </section>

  <div class="team">
    <figure class="member">
      <svg class="portrait" role="img" aria-label="Portrait photo of Callum Ferrier, Managing Director" viewBox="0 0 98 100">
        <defs><linearGradient id="pa" x1="0" y1="0" x2="0" y2="1"><stop offset="0" stop-color="#c98a62"/><stop offset="1" stop-color="#a46a48"/></linearGradient></defs>
        <rect width="98" height="100" fill="url(#pa)"/>
      </svg>
      <figcaption>Callum Ferrier<br><span class="role">Managing Director</span></figcaption>
    </figure>
    <figure class="member">
      <svg class="portrait" role="img" aria-label="Portrait photo of Graham Ferrier, Director" viewBox="0 0 98 100">
        <defs><linearGradient id="pb" x1="0" y1="0" x2="0" y2="1"><stop offset="0" stop-color="#b07a62"/><stop offset="1" stop-color="#4a3a36"/></linearGradient></defs>
        <rect width="98" height="100" fill="url(#pb)"/>
      </svg>
      <figcaption>Graham Ferrier<br><span class="role">Director</span></figcaption>
    </figure>
  </div>

  <div class="web left">www.harbourquarrycraft.com.au</div>
  <div class="web right">www.harbourquarrycraft.com.au</div>

  <div class="bottom-band outer"></div>
  <div class="bottom-band inner"></div>
</body>
</html>
```